Water Damage? Call Us!!

We are an established water damage mitigation company opening a storm chasing division. We will need the flyer to express urgency to call for water damage structural drying and demolition. I have attached our logo in various formats.

Check out our website for some ideas of what we do. www.blueheronrestoration.example

Include:

Blue Heron Restoration, LLC
Office@BlueHeronRestoration.example
www.blueheronrestoration.example
877-FLOOD-FIX
877-356-6349

I don't want to have our locations on there.

Target Market(s)

When someone has water damage to their home or business, we remove the wet material and then use fans and dehumidifiers to remove the moisture from the structure. We are like a Kelvane, but better. Lol

Colors

Designer to choose colors to be used in the design.

Requirements
Must have
• I have included various certification logos to use.
• Water damage must be the main focal point.
• We need to call them to action by calling us to dry their property. We will be dropping these flyers off in damaged areas.
• Trained in Drying Science by the NRSTB
• We handle Residential, Commercial, Hotels, Multi-Family.
• We specialize in Insurance Claims.
• We can bill your insurance company directly.
• Our Services include:
• Water Extraction/Muck Out
• Deconstruction of Damaged Materials
• Structural Drying
• Anti-Microbial Application
• Roofing
Nice to have
• It would be nice to have some thermal images of wet areas
Should not have
• Not looking for a fun flyer. These potential clients have suffered from devastation and we are looking to help them by getting their home or business back to normal.

```html
<!DOCTYPE html>
<html lang="en">
<head>
<meta charset="utf-8">
<title>Blue Heron Restoration – Water Damage Flyer</title>
<link href="https://fonts.googleapis.com/css2?family=Anton&family=Montserrat:wght@500;600;700;800&display=swap" rel="stylesheet">
<style>
:root{
  --stage:#2a3470;
  --navy:#0d1f8c;
  --ink:#1b2340;
  --sky:#1aa3ec;
  --sky-dark:#0a7fd0;
  --pale:#e6f4fc;
  --paper:#f7fbfe;
  --white:#ffffff;
}
*{box-sizing:border-box;margin:0;padding:0}
html,body{width:1200px;height:857px;overflow:hidden}
body{background:var(--stage);font-family:"Montserrat",sans-serif;position:relative}
.page{position:absolute;top:78px;width:540px;height:700px;overflow:hidden;background:var(--paper)}
.page--front{left:40px}
.page--back{left:620px}
.page svg.art{position:absolute;inset:0}

/* front */
.cover-photo{position:absolute;left:0;top:0;width:540px;height:460px;clip-path:path('M0,0 H540 V260 C380,400 180,440 0,400 Z');background:linear-gradient(180deg,#3d5f86 0%,#8b8f93 40%,#e2a24a 62%,#3a2c1f 88%)}
.brand{position:absolute;top:62px;left:36px;display:flex;align-items:center;gap:10px}
.brand__dot{width:34px;height:34px;border-radius:50%;background:var(--sky)}
.brand__name{font-weight:800;font-size:26px;line-height:1;color:var(--white);text-transform:uppercase;letter-spacing:.5px;max-width:260px}
.headline{position:absolute;left:36px;top:518px;font-family:"Anton",sans-serif;font-weight:400;font-size:70px;line-height:1;color:var(--navy);letter-spacing:.5px}
.subhead{position:absolute;left:38px;top:596px;font-family:"Anton",sans-serif;font-weight:400;font-size:30px;line-height:1;color:var(--sky);letter-spacing:.5px}
.front-url{position:absolute;left:40px;top:642px;font-weight:800;font-size:19px;color:var(--ink)}

/* back */
.focal{position:absolute;top:30px;left:26px;width:250px;font-weight:800;font-size:15px;line-height:1.25;color:var(--navy)}
.ticks{list-style:none;font-size:11px;line-height:1.35;color:var(--ink);font-weight:500}
.ticks li{position:relative;padding-left:18px;margin-bottom:6px}
.ticks li::before{content:"";position:absolute;left:0;top:3px;width:9px;height:5px;border-left:2px solid var(--sky);border-bottom:2px solid var(--sky);transform:rotate(-45deg)}
.intro{position:absolute;top:84px;left:26px;width:250px}
.block-title{font-weight:800;font-size:19px;line-height:1.1;color:var(--sky-dark);margin-bottom:10px}
.block-title--navy{color:var(--navy)}
.services{position:absolute;top:300px;left:40px;width:240px}
.certified{position:absolute;top:458px;left:40px;width:190px}
.photo-grid{position:absolute;top:40px;left:290px;width:230px;height:160px;display:grid;grid-template-columns:1fr 1fr;grid-template-rows:1fr 1fr;gap:4px}
.photo{border-radius:2px}
.photo--pipe{background:linear-gradient(135deg,#c2202a,#7d1118)}
.photo--house{background:linear-gradient(160deg,#b9d2e6,#c9a47d)}
.photo--wall{background:linear-gradient(135deg,#6a5a4b,#2d2722)}
.photo--fans{background:linear-gradient(160deg,#d9d3c3,#1f6fd1)}
.badges{position:absolute;top:220px;left:290px;width:210px;display:grid;grid-template-columns:repeat(3,1fr);gap:10px 8px;justify-items:center}
.badge{width:52px;height:52px;border-radius:50%;background:#9a9384}
.badge--green{background:#2f7d44}
.badge--square{border-radius:4px;background:#c2762e}
.badge--gold{border-radius:4px;background:#b68a3a}
.badge--ring{background:conic-gradient(#e63a7a,#f5b82e,#3fb34f,#1aa3ec,#e63a7a)}
.badge--wide{width:64px;border-radius:4px;background:#4b3f36}
.badge--seal{background:#3a3f4a}
.contact{position:absolute;left:325px;top:566px;width:210px;color:var(--white)}
.contact__name{display:flex;align-items:center;gap:8px;font-weight:800;font-size:16px;line-height:1.05;text-transform:uppercase;margin-bottom:8px}
.contact__dot{flex:none;width:20px;height:20px;border-radius:50%;background:var(--white)}
.contact__line{font-size:10px;font-weight:600;line-height:1.45;white-space:nowrap}
</style>
</head>
<body>

<section class="page page--front" aria-label="Flyer front">
  <svg class="art" viewBox="0 0 540 700" aria-hidden="true">
    <defs>
      <linearGradient id="frontBg" x1="0" y1="0" x2="0" y2="1">
        <stop offset="0" stop-color="#ffffff"/><stop offset="1" stop-color="#cfe9f8"/>
      </linearGradient>
    </defs>
    <rect width="540" height="700" fill="url(#frontBg)"/>
    <path d="M0,400 C180,450 380,400 540,260 L540,300 C400,440 200,480 0,450 Z" fill="#0a1a55"/>
    <path d="M0,440 C200,490 400,430 540,300 L540,350 C410,480 190,520 0,490 Z" fill="#1aa3ec"/>
    <path d="M0,505 C200,495 420,450 540,380" stroke="#0d1f8c" stroke-width="2" fill="none"/>
  </svg>
  <div class="cover-photo" role="img" aria-label="Photo of a drone flying over a storm-damaged building site at sunset"></div>
  <div class="brand"><span class="brand__dot"></span><span class="brand__name">Blue Heron Restoration</span></div>
  <h1 class="headline">Water Damage</h1>
  <p class="subhead">Structural Drying &amp; Demolition</p>
  <p class="front-url">www.blueheronrestoration.example</p>
</section>

<section class="page page--back" aria-label="Flyer back">
  <svg class="art" viewBox="0 0 540 700" aria-hidden="true">
    <rect width="540" height="700" fill="#f7fbfe"/>
    <path d="M0,0 H540 V40 C360,20 160,60 0,120 Z" fill="#e6f4fc"/>
    <circle cx="600" cy="700" r="350" fill="#1aa3ec"/>
    <circle cx="600" cy="700" r="332" fill="none" stroke="#ffffff" stroke-width="5"/>
  </svg>
  <h2 class="focal">Water Damage Must Be The Main Focal Point.</h2>
  <ul class="ticks intro">
    <li>We need to call them to action by calling us to dry their property. We will be dropping these flyers off in damaged areas.</li>
    <li>Trained in Drying Science by the NRSTB.</li>
    <li>We handle Residential, Commercial, Hotels, Multi-Family.</li>
    <li>We specialize in Insurance Claims.</li>
    <li>We can bill your insurance company directly.</li>
  </ul>
  <div class="photo-grid">
    <div class="photo photo--pipe" role="img" aria-label="Photo of a burst pipe spraying water"></div>
    <div class="photo photo--house" role="img" aria-label="Photo of a damaged house roof"></div>
    <div class="photo photo--wall" role="img" aria-label="Photo of a water-damaged wall cavity"></div>
    <div class="photo photo--fans" role="img" aria-label="Photo of drying fans lined up outside"></div>
  </div>
  <div class="badges" aria-label="Certifications">
    <span class="badge"></span><span class="badge badge--green"></span><span class="badge badge--square"></span>
    <span class="badge badge--gold"></span><span class="badge badge--ring"></span><span class="badge badge--wide"></span>
    <span class="badge badge--seal"></span><span class="badge badge--gold"></span>
  </div>
  <div class="services">
    <h3 class="block-title">Our Services Include:</h3>
    <ul class="ticks">
      <li>Water Extraction/Muck Out</li>
      <li>Deconstruction of Damaged Materials</li>
      <li>Structural Drying</li>
      <li>Anti-Microbial Application</li>
      <li>Roofing</li>
    </ul>
  </div>
  <div class="certified">
    <h3 class="block-title block-title--navy">NRSTB Certified</h3>
    <ul class="ticks">
      <li>24/7 Live Calls</li>
      <li>Onsite in 60 Minutes or less</li>
      <li>We bill directly to insurance</li>
      <li>Family Owned and operated</li>
      <li>We stay in communication with you throughout the process</li>
    </ul>
  </div>
  <div class="contact">
    <p class="contact__name"><span class="contact__dot"></span>Blue Heron Restoration</p>
    <p class="contact__line">Office@BlueHeronRestoration.example</p>
    <p class="contact__line">www.blueheronrestoration.example</p>
    <p class="contact__line">877-FLOOD-FIX</p>
    <p class="contact__line">877-356-6349</p>
  </div>
</section>

</body>
</html>
```